New Construction company looking for powerful bold logo. people see the logo, leaves an impression

We need a business card for our new company. We provide site work for commercial projects in South Texas. We clear land, excavation, run under ground utilities, concrete work, dirt work etc. We like the black card. I created a webpage www.tavo-lbuilders.com .... As I grow with projects I will put up pictures with video, and intro music. Want it look cool, bold, powerful, and slick looking. Creating 'TLB'....as my logo (possibly or if you have something you want to have fun with). Just have fun!!....thank you!

Darren Whitcombe Business Manager Serving South Texas PO Box 4387 Robstown,TX. 78380 Mobile: 361-752-9086 www.tavo-lbuilders.com darren@tavo-lbuilders.com you can put this anyway you see fit in your design and layout. thank you

Target Market(s)

General Contractors; Home Builders;

Industry/Entity Type

Construction

Contact Information for Business Card

I want the card to be black.

Font styles to use
Other font styles liked:
• Designer choice

Requirements
Must have
• Tavo-L Construction
• Site Work - Utilities/Concrete/Pad/Grading/Excavation (on the back side)
Nice to have
• Maybe TLB as the logo.....or just a symbol that would be TL.....and then construction to tie it togther...

```html
<!DOCTYPE html>
<html lang="en">
<head>
<meta charset="utf-8">
<title>Tavo-L Construction – Business Card</title>
<link rel="stylesheet" href="https://fonts.googleapis.com/css2?family=PT+Serif:wght@400;700&family=Source+Sans+3:wght@400&display=swap">
<style>
  :root {
    --stage: #000000;
    --card-black: #1e1e1e;
    --gold: #e2a92c;
    --white: #ffffff;
    --ink: #111111;
  }
  * { margin: 0; padding: 0; box-sizing: border-box; }
  html, body {
    width: 1200px; height: 1200px; overflow: hidden;
    background: var(--stage);
  }
  .canvas {
    position: relative; width: 1200px; height: 1200px;
  }
  .card {
    position: absolute; top: 444px;
    width: 549px; height: 313px;
    background: var(--card-black);
    overflow: hidden;
  }
  .card--front { left: 38px; }
  .card--back { left: 619px; }
  .card__shape {
    position: absolute; inset: 0; width: 100%; height: 100%;
  }
  .holder-name {
    position: absolute; left: 35px; top: 34px;
    font: 700 36px/1 "PT Serif", serif;
    color: var(--white);
  }
  .holder-title {
    position: absolute; left: 37px; top: 80px;
    font: 400 14.5px/1 "PT Serif", serif;
    color: var(--gold);
  }
  .services {
    position: absolute; list-style: none;
    font: 400 16px/22px "PT Serif", serif;
    color: var(--white);
  }
  .services li::before {
    content: "•"; display: inline-block; width: 14px; font-size: 13px;
  }
  .services--first { left: 44px; top: 118px; }
  .services--second { left: 193px; top: 130px; }
  .contact {
    position: absolute; left: 36px;
    display: flex; align-items: center; gap: 10px;
    font: 400 17.5px/1 "Source Sans 3", sans-serif;
    color: var(--gold);
  }
  .contact svg { width: 15px; height: 15px; flex: none; }
  .contact--phone { top: 206px; }
  .contact--email { top: 237px; }
  .rule {
    position: absolute; left: 34px; top: 275px;
    width: 256px; height: 3px; background: var(--gold);
  }
  .brand-name {
    position: absolute; text-align: center;
    font: 700 22px/1.1 "PT Serif", serif;
  }
  .brand-name--front { left: 390px; top: 198px; width: 160px; color: var(--ink); }
  .brand-name--back {
    left: 0; right: 0; top: 104px;
    font-size: 46px; color: var(--gold);
  }
</style>
</head>
<body>
<main class="canvas">

  <section class="card card--front">
    <svg class="card__shape" viewBox="0 0 549 313" preserveAspectRatio="none" aria-hidden="true">
      <path d="M424 0 Q414 210 311 313 L549 313 L549 0 Z" fill="var(--gold)"/>
    </svg>
    <h1 class="holder-name">Marcus Delgado</h1>
    <p class="holder-title">Project Manager</p>
    <ul class="services services--first">
      <li>Utilities</li>
      <li>Concrete</li>
      <li>Pad</li>
    </ul>
    <ul class="services services--second">
      <li>Grading</li>
      <li>Excavation</li>
    </ul>
    <p class="contact contact--phone">
      <svg viewBox="0 0 24 24" aria-hidden="true"><path fill="var(--white)" d="M6.6 10.8a15.1 15.1 0 0 0 6.6 6.6l2.2-2.2a1 1 0 0 1 1-.25 11.4 11.4 0 0 0 3.6.57 1 1 0 0 1 1 1V20a1 1 0 0 1-1 1A17 17 0 0 1 3 4a1 1 0 0 1 1-1h3.5a1 1 0 0 1 1 1c0 1.25.2 2.45.57 3.57a1 1 0 0 1-.25 1z"/></svg>
      (361) 752-9086
    </p>
    <p class="contact contact--email">
      <svg viewBox="0 0 24 24" aria-hidden="true"><rect x="2.5" y="5" width="19" height="14" fill="none" stroke="var(--white)" stroke-width="1.8"/><path d="M2.5 5l9.5 8 9.5-8M2.5 19l7-6.5M21.5 19l-7-6.5" fill="none" stroke="var(--white)" stroke-width="1.8"/></svg>
      bids@tavo-lbuilders.com
    </p>
    <div class="rule"></div>
    <p class="brand-name brand-name--front">Tavo-L<br>Construction</p>
  </section>

  <section class="card card--back">
    <svg class="card__shape" viewBox="0 0 549 313" preserveAspectRatio="none" aria-hidden="true">
      <rect width="549" height="313" fill="var(--gold)"/>
      <path d="M109 0 L549 0 L549 200 Q525 300 437 313 L0 313 L0 160 Q8 18 109 0 Z" fill="var(--card-black)"/>
    </svg>
    <p class="brand-name brand-name--back">Tavo-L<br>Construction</p>
  </section>

</main>
</body>
</html>
```